New Stationery and envelope Design Project

I need business envelopes and stationary. I would like to have office locations on both (only Chicago address) which are Chicago (Oak Brook), Denver, Monterrey, Lima. Of course in formats I can upload and have printed. Simple and very professional I am looking for. The return address/stationary address should be:

2870 North Fenwick Avenue
Tower Floor
Oak Brook, Illinois 60581

Target Market(s)

I am a consultant for larger corporations

Industry/Entity Type

Consulting

Colors

Designer to choose colors to be used in the design.

Requirements
Must have
• our address, logo, very professional and clean.
Nice to have
• the names of the cities we have offices.

```html
<!DOCTYPE html>
<html lang="en">
<head>
<meta charset="utf-8">
<title>Halsted Ridge Group – Business Cards</title>
<link href="https://fonts.googleapis.com/css2?family=Open+Sans:wght@400;600;700&display=swap" rel="stylesheet">
<style>
  :root {
    --bg: #d9dadc;
    --royal: #0b4fc2;
    --royal-deep: #0840a8;
    --sky: #3aa6e6;
    --sky-light: #8fd0f2;
    --paper: #ffffff;
    --paper-shade: #eceef0;
    --white-text: #ffffff;
  }
  * { margin: 0; padding: 0; box-sizing: border-box; }
  html, body { width: 1200px; height: 904px; overflow: hidden; }
  body {
    background: var(--bg);
    font-family: "Open Sans", Arial, sans-serif;
    position: relative;
  }
  .card {
    position: absolute;
    left: 250px;
    width: 700px;
    height: 400px;
    overflow: hidden;
    box-shadow: 0 6px 18px rgba(0,0,0,0.25);
  }
  /* Back side */
  .card--back {
    top: 36px;
    background: linear-gradient(160deg, var(--royal) 0%, var(--royal-deep) 100%);
  }
  .world-map {
    position: absolute;
    left: 60px; top: 40px;
    width: 580px; height: 260px;
    border-radius: 40px;
    background: radial-gradient(ellipse at center, rgba(90,150,235,0.55) 0%, rgba(60,120,220,0.25) 60%, rgba(11,79,194,0) 100%);
  }
  .back-brand {
    position: absolute;
    left: 0; right: 0; top: 118px;
    display: flex; flex-direction: column; align-items: center;
  }
  .brand-dot {
    width: 70px; height: 70px; border-radius: 50%;
    background: var(--sky);
  }
  .brand-name {
    font-weight: 400;
    font-size: 24px;
    letter-spacing: 0.5px;
    color: var(--royal);
  }
  .office-list {
    position: absolute;
    left: 0; right: 0; bottom: 34px;
    text-align: center;
    color: var(--white-text);
    font-weight: 700;
    font-size: 17px;
    letter-spacing: 0.2px;
  }
  .office-list .sep { font-weight: 400; margin: 0 6px; opacity: 0.85; }

  /* Front side */
  .card--front {
    top: 468px;
    background: linear-gradient(135deg, var(--paper) 0%, var(--paper-shade) 100%);
  }
  .card--front svg.panel { position: absolute; inset: 0; }
  .front-brand {
    position: absolute;
    left: 40px; top: 120px;
    width: 300px;
    display: flex; flex-direction: column; align-items: center; gap: 18px;
  }
  .front-brand .brand-dot { width: 86px; height: 86px; }
  .contact {
    position: absolute;
    left: 490px; top: 56px;
    color: var(--white-text);
    font-size: 15px;
    line-height: 1.45;
  }
  .contact__name {
    color: var(--sky);
    font-size: 19px;
    font-weight: 600;
    letter-spacing: 0.5px;
  }
  .contact__role { font-size: 15px; margin-bottom: 16px; }
  .contact__address { margin-bottom: 16px; }
  .contact__line { display: flex; align-items: center; gap: 8px; }
  .contact__line svg { width: 13px; height: 13px; flex: none; }
</style>
</head>
<body>

  <section class="card card--back" aria-label="Card back">
    <div class="world-map" role="img" aria-label="Dotted world map in light blue"></div>
    <div class="back-brand">
      <span class="brand-dot"></span>
    </div>
    <p class="office-list">Chicago (Oak Brook)<span class="sep">|</span>Denver<span class="sep">|</span>Monterrey<span class="sep">|</span>Lima</p>
  </section>

  <section class="card card--front" aria-label="Card front">
    <svg class="panel" width="700" height="400" viewBox="0 0 700 400">
      <path d="M300 0 C430 60 470 250 420 400 L700 400 L700 0 Z" fill="#0b4fc2"/>
      <path d="M300 0 C430 60 470 250 420 400" fill="none" stroke="#8fd0f2" stroke-width="14"/>
      <path d="M318 4 C444 66 482 250 436 400" fill="none" stroke="#3aa6e6" stroke-width="6"/>
      <path d="M336 10 C458 74 494 250 452 400" fill="none" stroke="#0840a8" stroke-width="4"/>
    </svg>

    <div class="front-brand">
      <span class="brand-dot"></span>
      <span class="brand-name">HALSTED RIDGE GROUP</span>
    </div>

    <div class="contact">
      <p class="contact__name">DANIEL REYES</p>
      <p class="contact__role">Manager</p>
      <p class="contact__address">2870 North Fenwick Avenue<br>Tower Floor<br>Oak Brook, Illinois 60581</p>
      <p class="contact__line">
        <svg viewBox="0 0 16 16"><circle cx="8" cy="8" r="8" fill="#3aa6e6"/><path d="M5 4.5l1.6 0 .7 2-1 .8a6 6 0 0 0 2.4 2.4l.8-1 2 .7 0 1.6c-3.7.3-6.8-2.8-6.5-6.5z" fill="#0b4fc2"/></svg>
        +1 630 555 0148
      </p>
      <p class="contact__line">
        <svg viewBox="0 0 16 16"><circle cx="8" cy="8" r="8" fill="#3aa6e6"/><rect x="4" y="5" width="8" height="6" fill="#0b4fc2"/><path d="M4 5l4 3.5L12 5" fill="none" stroke="#8fd0f2" stroke-width="1"/></svg>
        info@halstedridge.com
      </p>
      <p class="contact__line">
        <svg viewBox="0 0 16 16"><circle cx="8" cy="8" r="8" fill="#3aa6e6"/><circle cx="8" cy="8" r="4" fill="none" stroke="#0b4fc2" stroke-width="1.2"/><path d="M4 8h8M8 4v8" stroke="#0b4fc2" stroke-width="1"/></svg>
        www.halstedridge.com
      </p>
    </div>
  </section>

</body>
</html>
```